依頼詳細
神奈川県横浜市に2店舗展開する美容室です。

今年で5回目のクリスマスDM依頼となります。

小さいお子様から70代ぐらいの方まで幅広い世代にご利用いただいております。
なかでも30代40代の美意識の高い大人の女性をメインターゲットにしています。

2店舗ともそれぞれサロンの雰囲気が異なりますので、
ぜひHPを参考にご覧ください。

今年もクリスマスDMのポストカードデザインをお願いいたします。
2店舗同じものを使いたいと思っています。

美容室ですが、美容室っぽさはデザインの中に取り込まなくても結構です。

イメージ的には、
堅苦しくなく、
家族や友人から送られてきたのかな??
と感じるような、
女性目線のシンプルかつオシャレなデザインが希望です。

また、オリジナル性を重視しますので、
ロゴもしくは店名(lumo)をデザインの中に取り入れていただきたいです。

過去の作品なども参考にしていただけたらと思います。

締切日が短く恐縮ではございますが、
宜しくお願いいたします。
記載項目
表面(切手を貼る側)デザインにコメント・年末年始のお休みのお知らせ・2店舗の店名住所電話番号の記載をお願いします。手書きコメントスペースがほしいです。
【コメント】日頃のご愛顧、誠にありがとうございます。皆様の笑顔の為に素敵なヘアデザインと最高の満足をお届けできるように、技術の向上とサービスに努めてまいります。lumoスタッフ一同、心よりお待ちしております。
【年末年始休み】12/24(火)定休日 25(水)~30(月)通常営業 31(火)~1/4(土)正月休み 5(日)より 通常営業
【住所など】lumoPLUS 横浜市西区岡野3-4-8-1F TEL 045-587-2140 verde by lumo 横浜市中区住吉町2-48みなとグランドビル桜通1F TEL045-323-9807
【URL】http://lumo-salon.example
裏面:ロゴもしくは店名(lumo)イラスト
希望イメージ
シンプル 複雑
単色 カラフル
暗い 明るい
日常 高級
遊び心 厳粛
未来的 伝統的
女性的 男性的
希望する色
設定なし
納品ファイル
• 高解像度JPG (.jpg)
• イラストレーター形式 (.ai)
補足説明
印刷を「ミナプリ」さんにお願いを予定しています。入稿前チェックガイドのご確認よろしくお願い致します。
https://help.minapuri.example/guide/data-check-guide/?_ga=1.518204736.302948571.1583920462
■ 選んだ理由

スタッフ全員による投票の結果、決めさせていただきました。
イラストタッチでかわいらしく、女性の方に喜んで頂けそうなデザインが気に入っております。

■ 提案者全員のお礼・コメント

今年もたくさんの素敵なデザイン提案いただきましてありがとうございます。
幸せな事に厳選させて頂くことが難しく感謝いたしております。
またの機会がございましたら、よろしくお願い申し上げます。

```html
<!DOCTYPE html>
<html lang="en">
<head>
<meta charset="utf-8">
<title>Merry Christmas – lumo</title>
<link rel="stylesheet" href="https://fonts.googleapis.com/css2?family=Great+Vibes&family=Raleway:wght@300;400&display=swap">
<style>
  :root {
    --card-red: #e2483f;
    --stripe-red: #e95a50;
    --paper: #ffffff;
    --gold: #c9a04a;
    --ink: #3a3a3a;
    --blush: #f6cfc8;
    --wreath-cream: #f6f1ea;
    --wreath-blush: #efc3b6;
    --wreath-green: #7aa583;
    --wreath-deep: #4f8a66;
  }
  * { margin: 0; padding: 0; box-sizing: border-box; }
  html, body { width: 811px; height: 1200px; overflow: hidden; }
  body { background: var(--card-red); }

  .card {
    position: relative;
    width: 811px;
    height: 1200px;
    background:
      repeating-linear-gradient(90deg,
        var(--card-red) 0 34px,
        var(--stripe-red) 34px 48px,
        var(--card-red) 48px 70px,
        var(--stripe-red) 70px 76px);
    overflow: hidden;
  }

  .wreath {
    position: absolute;
    left: 44px;
    top: 138px;
    width: 726px;
    height: 766px;
    border-radius: 46%;
    background:
      radial-gradient(ellipse closest-side at 50% 50%,
        var(--wreath-cream) 0%,
        var(--wreath-cream) 58%,
        var(--wreath-blush) 74%,
        var(--wreath-green) 90%,
        var(--wreath-deep) 100%);
  }

  .greeting-panel {
    position: absolute;
    left: 184px;
    top: 272px;
    width: 446px;
    height: 506px;
    background: var(--paper);
  }
  .greeting-panel__frame {
    position: absolute;
    inset: 16px;
    border: 2px solid var(--gold);
  }

  .greeting-title {
    position: absolute;
    left: 0;
    right: 0;
    top: 78px;
    text-align: center;
    font-family: "Great Vibes", cursive;
    font-weight: 400;
    color: var(--gold);
    font-size: 104px;
    line-height: 154px;
  }

  .salon-name {
    position: absolute;
    left: 0;
    right: 0;
    top: 428px;
    text-align: center;
    font-family: "Raleway", sans-serif;
    font-weight: 400;
    font-size: 36px;
    line-height: 48px;
    letter-spacing: 1px;
    color: var(--ink);
  }

  .new-year-line {
    position: absolute;
    left: 0;
    right: 0;
    top: 996px;
    text-align: center;
    font-family: "Raleway", sans-serif;
    font-weight: 300;
    font-size: 30px;
    line-height: 36px;
    letter-spacing: 3px;
    color: var(--blush);
  }
</style>
</head>
<body>
  <main class="card">
    <div class="wreath" role="img" aria-label="Illustrated wreath of white poinsettias, red berries, pine cones and green winter foliage framing the greeting"></div>

    <section class="greeting-panel">
      <div class="greeting-panel__frame"></div>
      <h1 class="greeting-title">Merry<br>Christmas</h1>
      <p class="salon-name">lumo</p>
    </section>

    <p class="new-year-line">AND HAPPY NEW YEAR</p>
  </main>
</body>
</html>
```